Brightline Power Crew, LLC New Business Card Design Project

Please do not submit multiple designs that look similar. Many submittals of nearly the same design will result in auto rejection. Please do not submit a design unless you know how to provide a PDF with recognizable text that I can modify and update using Adobe Acrobat. I do not use Adobe Photoshop. Please design a business card using the attached BPC logo. Be creative. Do at least 2-3 different designs. One side should have the logo large with the URL www.BPC-RT.com. The other side of the card should have the name Marcus Pellham. License number 524318. Phone number 555-555-0147. Email service@BPC-RT.com. Physical address 742 Fenwick Orchard Road, Suite 5, Maplebrook, NR. 06981. The company name should also be spelled out somewhere, Brightline Power Crew, LLC. Please ensure there is no tiny font. Please also ensure that there is nothing near the edges that might get cut off during printing. It will be 3.5" x 2" horizontal standard business card. I use CardMintly.com to order. The customer has said they want the business card to use the attached look and color scheme. Please do not submit a design unless you know how to provide a PDF with recognizable text that I can modify and update using Adobe Acrobat. I do not use Adobe Photoshop.
Target Market(s)
Read all instructions above.
Industry/Entity Type
Contact Information for Business Card
Requirements
Must have
- Read all instructions above.
Nice to have
Should not have

```html
<!DOCTYPE html>
<html lang="en">
<head>
<meta charset="utf-8">
<title>Brightline Power Crew, LLC – Business Card</title>
<link href="https://fonts.googleapis.com/css2?family=Poppins:wght@500;600;700&display=swap" rel="stylesheet">
<style>
  :root {
    --backdrop: #3b3b3d;
    --card: #141414;
    --gold: #e2b51f;
    --white: #f4f4f4;
  }
  * { box-sizing: border-box; margin: 0; padding: 0; }
  html, body {
    width: 1200px; height: 801px; overflow: hidden;
    background: var(--backdrop);
    font-family: "Poppins", sans-serif;
  }
  .sheet {
    width: 1200px; height: 801px;
    display: flex; align-items: center; justify-content: center; gap: 40px;
  }
  .card {
    position: relative;
    width: 540px; height: 309px;
    background: var(--card);
    border-radius: 22px;
    box-shadow: 0 10px 30px rgba(0,0,0,.45);
  }

  /* Front side */
  .card-front { display: flex; flex-direction: column; align-items: center; justify-content: center; gap: 18px; }
  .brand-mark { display: flex; align-items: center; gap: 16px; }
  .brand-mark .dot { width: 26px; height: 26px; border-radius: 50%; background: var(--gold); }
  .brand-mark .name { color: var(--gold); font-weight: 700; font-size: 92px; line-height: 1; letter-spacing: 2px; }
  .front-url { color: var(--gold); font-weight: 600; font-size: 17px; letter-spacing: .5px; }

  /* Back side */
  .card-back { padding: 40px 36px; }
  .company { color: var(--gold); font-weight: 700; font-size: 27px; line-height: 1.1; }
  .license { color: var(--white); font-weight: 500; font-size: 13px; margin: 6px 0 0 108px; }
  .contact-list { position: absolute; right: 40px; top: 122px; list-style: none; }
  .contact-list li { display: flex; align-items: center; gap: 8px; color: var(--white); font-weight: 500; font-size: 13.5px; margin-bottom: 6px; }
  .contact-list svg { width: 14px; height: 14px; fill: var(--gold); flex: none; }
  .person { position: absolute; left: 36px; top: 178px; color: var(--gold); font-weight: 700; font-size: 30px; }
  .address { position: absolute; left: 36px; bottom: 34px; display: flex; align-items: center; gap: 8px; color: var(--white); font-weight: 500; font-size: 13.5px; }
  .address svg { width: 14px; height: 18px; fill: var(--gold); flex: none; }
</style>
</head>
<body>
<main class="sheet">
  <section class="card card-front" aria-label="Card front">
    <div class="brand-mark">
      <span class="dot"></span>
      <span class="name">BPC</span>
    </div>
    <p class="front-url">www.BPC-RT.com</p>
  </section>

  <section class="card card-back" aria-label="Card back">
    <h1 class="company">Brightline Power Crew, LLC</h1>
    <p class="license">License number 524318</p>

    <ul class="contact-list">
      <li>
        <svg viewBox="0 0 24 24" aria-hidden="true"><path d="M6.6 10.8a15.5 15.5 0 0 0 6.6 6.6l2.2-2.2a1 1 0 0 1 1-.25 11.4 11.4 0 0 0 3.6.57 1 1 0 0 1 1 1V20a1 1 0 0 1-1 1A17 17 0 0 1 3 4a1 1 0 0 1 1-1h3.5a1 1 0 0 1 1 1c0 1.25.2 2.45.57 3.57a1 1 0 0 1-.25 1z"/></svg>
        555-555-0147
      </li>
      <li>
        <svg viewBox="0 0 24 24" aria-hidden="true"><path d="M2 5h20v2l-10 7L2 7z M2 9l10 7 10-7v10H2z"/></svg>
        service@BPC-RT.com
      </li>
    </ul>

    <p class="person">Marcus Pellham</p>

    <p class="address">
      <svg viewBox="0 0 24 30" aria-hidden="true"><path d="M12 0a10 10 0 0 0-10 10c0 7.5 10 20 10 20s10-12.5 10-20A10 10 0 0 0 12 0zm0 14a4 4 0 1 1 0-8 4 4 0 0 1 0 8z"/></svg>
      742 Fenwick Orchard Road, Suite 5, Maplebrook, NR. 06981
    </p>
  </section>
</main>
</body>
</html>
```